Freelance business trainer needs a new business card

My business is called Tbrite. I provide training in the workplace on management, coaching and mentoring, and customer service topics for a variety of businesses, colleges and private training providers, and teach on management programs. I need a professional but eye catching business card. Business colours grey and orange. My name Linda Marchbank; Tel 07853 416207; email lmarchbank@tbrite.co.uk; website www.tbrite.co.uk.
Happy to have some sort of logo on front and details on back or all on one side
Target Market(s)
SME businesses and colleges - workshops i run are for adults in the workplace
Industry/Entity Type
Training
Look and feel

```html
<!DOCTYPE html>
<html lang="en">
<head>
<meta charset="utf-8">
<title>Tbrite – Business Card</title>
<link rel="stylesheet" href="https://fonts.googleapis.com/css2?family=Ubuntu:wght@400;500&family=Roboto+Condensed:wght@400&display=swap">
<style>
  :root {
    --orange: #e07318;
    --grey: #6f6f70;
    --band: #f8f6f0;
    --white: #ffffff;
    --backdrop: #ececef;
  }
  html, body {
    margin: 0;
    width: 1200px;
    height: 800px;
    overflow: hidden;
    background: var(--backdrop);
  }
  .card {
    position: absolute;
    left: 145px;
    top: 140px;
    width: 910px;
    height: 520px;
    background: var(--orange);
    box-shadow: 0 6px 18px rgba(0,0,0,0.18);
    overflow: hidden;
  }
  .card__rules {
    position: absolute;
    left: 268px;
    top: 0;
    width: 28px;
    height: 215px;
  }
  .brand {
    position: absolute;
    left: 100px;
    top: 258px;
    margin: 0;
    font-family: "Ubuntu", sans-serif;
    font-weight: 400;
    font-size: 58px;
    line-height: 1;
    color: var(--white);
  }
  .name-band {
    position: absolute;
    left: 462px;
    top: 118px;
    width: 448px;
    height: 62px;
    background: var(--band);
    box-shadow: -4px 14px 14px rgba(0,0,0,0.28);
    display: flex;
    align-items: center;
    padding-left: 32px;
    box-sizing: border-box;
  }
  .name-band__name {
    font-family: "Ubuntu", sans-serif;
    font-weight: 400;
    font-size: 27px;
    color: var(--orange);
  }
  .contacts {
    position: absolute;
    left: 484px;
    top: 245px;
    margin: 0;
    padding: 0;
    list-style: none;
  }
  .contacts__item {
    display: flex;
    align-items: center;
    height: 56px;
  }
  .contacts__icon {
    width: 26px;
    height: 26px;
    margin-right: 34px;
    fill: var(--grey);
  }
  .contacts__text {
    font-family: "Roboto Condensed", sans-serif;
    font-size: 29px;
    letter-spacing: 1px;
    color: var(--white);
  }
</style>
</head>
<body>
  <div class="card">
    <svg class="card__rules" viewBox="0 0 28 215" aria-hidden="true">
      <rect x="2" y="0" width="6" height="215" fill="var(--grey)"/>
      <rect x="20" y="0" width="6" height="215" fill="var(--grey)"/>
    </svg>

    <p class="brand">Tbrite</p>

    <div class="name-band">
      <span class="name-band__name">Linda Marchbank</span>
    </div>

    <ul class="contacts">
      <li class="contacts__item">
        <svg class="contacts__icon" viewBox="0 0 24 24" aria-hidden="true">
          <path d="M3 8c0-2 2-4 9-4s9 2 9 4v2h-5V8H8v2H3z"/>
          <path d="M6 11h12l2 9H4z"/>
        </svg>
        <span class="contacts__text">07853 416207</span>
      </li>
      <li class="contacts__item">
        <svg class="contacts__icon" viewBox="0 0 24 24" aria-hidden="true">
          <path d="M2 5h20v14H2z M3.5 6.5 12 13l8.5-6.5" stroke="var(--orange)" stroke-width="1.4"/>
        </svg>
        <span class="contacts__text">lmarchbank@tbrite.co.uk</span>
      </li>
      <li class="contacts__item">
        <svg class="contacts__icon" viewBox="0 0 24 24" aria-hidden="true">
          <circle cx="12" cy="12" r="10"/>
          <g fill="none" stroke="var(--orange)" stroke-width="1.3">
            <ellipse cx="12" cy="12" rx="4.5" ry="10"/>
            <path d="M2 12h20M4 7h16M4 17h16M12 2v20"/>
          </g>
        </svg>
        <span class="contacts__text">www.tbrite.co.uk.</span>
      </li>
    </ul>
  </div>
</body>
</html>
```